Zanquerra Business Card Design

Zanquerra is a small and new restaurant/ bar location in Hong Kong. The name "Djibouti" derives from an African country. There is no specific reason behind other than the fact, that the bar is somewhat inspired by African elements (only inspired but not purely based on African cuisine etc.).

The bar is somewhat a fusion of African, Mediterranean and Oriental (Old French Vietnam) elements.

However, it is very imperative to stress, that the overall look and feel of Zanquerra is a very high end cocktail lounge/ bar location. The bar is tucked away in a hidden alley, so people will have to know about it. The idea is to send the consumer off in an Escape or hidden remote location where they are at ease in a hip, stylish and trendy environment.

The card needs to feel high-end.

Final logo artwork has been attached and also pictures of the bar/ restaurant itself. The logo ie monkey head cannot be modified. However, the background color and the color of the type "ZANQUERRA" can be changed.

The following details need to fit onto the business card. Of course they can be arranged to your liking:

LOGO

Tobin Le
Partner

+852 90817364
xxx@zanquerra-bar.com
www.zanquerra-bar.com
4C, Pelham Lane, Wan Chai, Hong Kong

Industry/Entity Type

Restaurant

```html
<!DOCTYPE html>
<html lang="en">
<head>
<meta charset="utf-8">
<title>Zanquerra Business Card</title>
<link rel="stylesheet" href="https://fonts.googleapis.com/css2?family=Open+Sans:wght@400;600;700&display=swap">
<style>
  :root {
    --page-bg: #e6e6e6;
    --card-red: #c8161d;
    --card-red-mid: #b81219;
    --card-red-deep: #a80f16;
    --card-white: #ffffff;
    --ink: #1c1c1c;
    --ink-soft: #555555;
    --accent-blue: #2a9ad8;
    --mark-dark: #161616;
  }
  * { box-sizing: border-box; margin: 0; padding: 0; }
  html, body { width: 1200px; height: 1200px; overflow: hidden; }
  body {
    background: var(--page-bg);
    font-family: "Open Sans", Arial, sans-serif;
    color: var(--ink);
    position: relative;
  }
  .card {
    position: absolute;
    left: 180px;
    width: 840px;
    height: 480px;
    box-shadow: 0 10px 30px rgba(0,0,0,0.18);
    overflow: hidden;
  }
  .card--front { top: 90px; background: var(--card-red); }
  .card--back { top: 630px; background: var(--card-white); }

  .front-texture {
    position: absolute;
    inset: 0;
    background: linear-gradient(135deg, var(--card-red) 0%, var(--card-red-mid) 50%, var(--card-red-deep) 100%);
  }

  .brand-disc {
    position: absolute;
    border-radius: 50%;
    background: var(--mark-dark);
  }
  .brand-name {
    position: absolute;
    font-family: "Open Sans", Arial, sans-serif;
    font-weight: 700;
    color: var(--ink);
    letter-spacing: 3px;
    white-space: nowrap;
    line-height: 1;
  }
  .card--front .brand-disc { left: 470px; top: 120px; width: 170px; height: 170px; }
  .card--front .brand-name { left: 250px; top: 308px; font-size: 50px; }

  .card--back .brand-disc { left: 180px; top: 110px; width: 120px; height: 120px; }
  .card--back .brand-name { left: 60px; top: 246px; font-size: 36px; letter-spacing: 2px; }

  .divider {
    position: absolute;
    left: 420px; top: 70px;
    width: 3px; height: 320px;
    background: var(--accent-blue);
  }
  .contact {
    position: absolute;
    left: 445px; top: 70px;
    width: 370px;
  }
  .contact__name { font-weight: 600; font-size: 30px; line-height: 1.1; }
  .contact__role { font-size: 19px; color: var(--ink-soft); margin-bottom: 26px; }
  .contact__list { list-style: none; }
  .contact__item {
    display: flex; align-items: flex-start; gap: 10px;
    font-size: 20px; line-height: 1.3; margin-bottom: 6px;
  }
  .contact__icon { flex: 0 0 20px; width: 20px; height: 20px; margin-top: 3px; }
</style>
</head>
<body>

<section class="card card--front" aria-label="Card front">
  <div class="front-texture" role="img" aria-label="Fine red diagonal lattice pattern covering the card front"></div>
  <span class="brand-disc" aria-hidden="true"></span>
  <span class="brand-name">ZANQUERRA</span>
</section>

<section class="card card--back" aria-label="Card back">
  <span class="brand-disc" aria-hidden="true"></span>
  <span class="brand-name">ZANQUERRA</span>
  <span class="divider" aria-hidden="true"></span>
  <div class="contact">
    <p class="contact__name">Tobin Le</p>
    <p class="contact__role">Partner</p>
    <ul class="contact__list">
      <li class="contact__item">
        <svg class="contact__icon" viewBox="0 0 20 20" aria-hidden="true"><path d="M10 2 L19 10 H16 V18 H12 V13 H8 V18 H4 V10 H1 Z" fill="#2a9ad8"/></svg>
        <span>4C, Pelham Lane, Wan Chai,<br>Hong Kong</span>
      </li>
      <li class="contact__item">
        <svg class="contact__icon" viewBox="0 0 20 20" aria-hidden="true"><rect width="20" height="20" rx="3" fill="#2a9ad8"/><path d="M6 4 L9 4 L10 7 L8 8.5 Q9.5 11.5 11.5 12 L13 10 L16 11 L16 14 Q10 16 6 10 Q4 7 6 4Z" fill="#fff"/></svg>
        <span>+852 90817364</span>
      </li>
      <li class="contact__item">
        <svg class="contact__icon" viewBox="0 0 20 20" aria-hidden="true"><rect width="20" height="20" rx="3" fill="#2a9ad8"/><rect x="4" y="6" width="12" height="9" fill="none" stroke="#fff" stroke-width="1.5"/><path d="M4 6 L10 11 L16 6" fill="none" stroke="#fff" stroke-width="1.5"/></svg>
        <span>xxx@zanquerra-bar.com</span>
      </li>
      <li class="contact__item">
        <svg class="contact__icon" viewBox="0 0 20 20" aria-hidden="true"><rect width="20" height="20" rx="3" fill="#2a9ad8"/><circle cx="10" cy="10" r="6" fill="none" stroke="#fff" stroke-width="1.4"/><path d="M4 10 H16 M10 4 Q6.5 10 10 16 M10 4 Q13.5 10 10 16" fill="none" stroke="#fff" stroke-width="1.2"/></svg>
        <span>www.zanquerra-bar.com</span>
      </li>
    </ul>
  </div>
</section>

</body>
</html>
```